Managed IT services business card design

We haven't needed a business card since the founding of the business in 2005. All our clients have been coming through word of mouth. And lately more and more existing clients are requesting for our business cards to pass on to their contacts in recommending us.
So we needing a business card design. We use various innovative solutions and methodologies to provide IT services to small businesses in managing their IT systems. Our role is the same as an in-house, full-time IT Manager for our clients, but outsourced. So we take care of all our clients' IT needs, just as an IT Manager would be expected to perform.
We have a holding website, which we're happy to leave for now. If we can use the same logo would be great - www.lomvex.com.au
Preferred colours are shades of are white, grey and black.
We pride our business with the following traits: proactive, good service, prompt response, trustworthy.
Target Market(s)
Small businesses of any industry
Industry/Entity Type
Business

```html
<!DOCTYPE html>
<html lang="en">
<head>
<meta charset="utf-8">
<title>Lomvex business card</title>
<link href="https://fonts.googleapis.com/css2?family=Questrial&display=swap" rel="stylesheet">
<style>
  :root {
    --canvas: #dcdcdc;
    --paper: #ffffff;
    --slate: #5c5f64;
    --slate-dark: #53565b;
    --slate-light: #65686d;
    --ink: #111111;
    --text-light: #ffffff;
  }
  * { margin: 0; padding: 0; box-sizing: border-box; }
  html, body {
    width: 1200px;
    height: 680px;
    overflow: hidden;
    background: var(--canvas);
    font-family: "Questrial", "Century Gothic", sans-serif;
  }
  .canvas {
    position: relative;
    width: 1200px;
    height: 680px;
    display: flex;
    align-items: center;
    justify-content: center;
    gap: 60px;
  }
  .card {
    position: relative;
    width: 520px;
    height: 297px;
    overflow: hidden;
    box-shadow: 0 6px 18px rgba(0,0,0,0.18);
  }

  /* Front */
  .card-front { background: var(--paper); }
  .front-band {
    position: absolute;
    left: 0; right: 0;
    top: 122px;
    height: 134px;
    background: var(--slate);
  }
  .front-rule {
    position: absolute;
    left: 0; right: 0;
    top: 256px;
    height: 7px;
    border-top: 3px solid var(--ink);
    border-bottom: 1px solid var(--ink);
    background: var(--paper);
  }
  .wordmark {
    position: absolute;
    display: flex;
    align-items: center;
    gap: 22px;
  }
  .wordmark-name { letter-spacing: 0.32em; line-height: 1; }
  .wordmark-mark { display: block; }
  .card-front .wordmark { left: 46px; top: 62px; }
  .card-front .wordmark-name { font-size: 40px; color: var(--ink); }
  .card-front .wordmark-mark { width: 14px; height: 14px; background: var(--ink); }

  .contact-list {
    position: absolute;
    left: 26px;
    top: 166px;
    list-style: none;
    color: var(--text-light);
    font-size: 14px;
    line-height: 19px;
  }
  .contact-list li { display: flex; align-items: center; gap: 8px; }
  .contact-icon { width: 13px; height: 13px; flex: none; }

  .person {
    position: absolute;
    right: 28px;
    top: 134px;
    text-align: right;
    color: var(--text-light);
  }
  .person-name { font-size: 16px; line-height: 18px; }
  .person-role { font-size: 11px; line-height: 14px; }
  .person-address { margin-top: 26px; font-size: 13px; line-height: 16px; font-style: normal; }

  /* Back */
  .card-back {
    background: linear-gradient(135deg, var(--slate-light) 0%, var(--slate) 50%, var(--slate-dark) 100%);
  }
  .back-texture { position: absolute; inset: 0; width: 100%; height: 100%; }
  .card-back .wordmark { right: 44px; bottom: 72px; }
  .card-back .wordmark-name { font-size: 54px; color: var(--text-light); }
  .card-back .wordmark-mark { width: 16px; height: 16px; background: var(--text-light); }
  .back-web {
    position: absolute;
    right: 56px;
    bottom: 40px;
    color: var(--text-light);
    font-size: 14px;
    letter-spacing: 0.32em;
  }
</style>
</head>
<body>
<main class="canvas">

  <section class="card card-front" aria-label="Business card front">
    <div class="front-band"></div>
    <div class="front-rule"></div>

    <div class="wordmark">
      <span class="wordmark-name">lomvex</span>
      <span class="wordmark-mark" aria-hidden="true"></span>
    </div>

    <div class="person">
      <p class="person-name">Mark Tellaby</p>
      <p class="person-role">director</p>
      <address class="person-address">1450 Orin Vale Rd<br>Calder TX 70000</address>
    </div>

    <ul class="contact-list">
      <li>
        <svg class="contact-icon" viewBox="0 0 14 14" aria-hidden="true">
          <circle cx="7" cy="7" r="6.5" fill="#fff"/>
          <path d="M4.5 3.5c-.8.8-.6 2.6 1.2 4.6s3.6 2.3 4.3 1.5l-1.3-1.3-.9.6c-.8-.4-1.7-1.3-2.1-2.1l.6-.9z" fill="#5c5f64"/>
        </svg>
        <span>512 555 0140</span>
      </li>
      <li>
        <svg class="contact-icon" viewBox="0 0 14 14" aria-hidden="true">
          <rect x="1" y="6" width="12" height="6" rx="1" fill="#fff"/>
          <rect x="3.5" y="2" width="7" height="4" fill="#fff"/>
          <rect x="3" y="8" width="8" height="1" fill="#5c5f64"/>
        </svg>
        <span>512 555 0141</span>
      </li>
      <li>
        <svg class="contact-icon" viewBox="0 0 14 14" aria-hidden="true">
          <rect x="1" y="3" width="12" height="8" fill="#fff"/>
          <path d="M1 3l6 5 6-5" fill="none" stroke="#5c5f64" stroke-width="1"/>
        </svg>
        <span>info@lomvex.com</span>
      </li>
      <li>
        <svg class="contact-icon" viewBox="0 0 14 14" aria-hidden="true">
          <circle cx="7" cy="7" r="6" fill="#fff"/>
          <path d="M1 7h12M7 1v12M3 3.5c2.5 1.5 5.5 1.5 8 0M3 10.5c2.5-1.5 5.5-1.5 8 0" fill="none" stroke="#5c5f64" stroke-width="0.6"/>
        </svg>
        <span>www.lomvex.com</span>
      </li>
    </ul>
  </section>

  <section class="card card-back" aria-label="Business card back">
    <svg class="back-texture" viewBox="0 0 520 297" preserveAspectRatio="none" role="img" aria-label="Faint tonal background shapes">
      <rect width="520" height="297" fill="none"/>
    </svg>
    <div class="wordmark">
      <span class="wordmark-name">lomvex</span>
      <span class="wordmark-mark" aria-hidden="true"></span>
    </div>
    <p class="back-web">www.lomvex.com</p>
  </section>

</main>
</body>
</html>
```